Tulmex Business Card

I already have the conplay logo. I need to develop a professional business card layout

Target Market(s)

Business

Industry/Entity Type

Business

Contact Information for Business Card

Company Name: Tulmex Limited

Font styles to use
Sans Serif

Colors

Designer to choose colors to be used in the design.

Requirements
Must have
• Use current logo
• Need two card size options:
• Small Card: 70mm x 28mm (Landscape)
• Square Card: 65mm x 65mm
Nice to have
• I will need 8-10 files for each name, number and email address (details to follow)

```html
<!DOCTYPE html>
<html lang="en">
<head>
<meta charset="utf-8">
<title>Tulmex Limited – Business Cards</title>
<link rel="stylesheet" href="https://fonts.googleapis.com/css2?family=Questrial&family=Open+Sans:wght@400;700&display=swap">
<style>
  :root {
    --page: #ffffff;
    --ink: #231f20;
    --card-edge: #3a3a3a;
    --band-grey: #b3b3b3;
    --logo: #006b38;
    --t1: #004d29;
    --t2: #006b38;
    --t3: #2f8a55;
    --t4: #5ea873;
    --t5: #8cc58f;
    --t6: #c9c9c9;
    --t7: #b3b3b3;
    --t8: #999999;
    --t9: #7a7a7a;
    --t10: #5c5c5c;
  }
  * { box-sizing: border-box; margin: 0; padding: 0; }
  html, body { width: 1200px; height: 1000px; overflow: hidden; background: var(--page); }
  body { position: relative; font-family: "Questrial", "Century Gothic", sans-serif; color: var(--ink); }

  .card { position: absolute; background: #fff; overflow: hidden; }
  .card--small { left: 308px; top: 79px; width: 584px; height: 234px; border: 1px solid var(--card-edge); }
  .card--square { left: 329px; top: 379px; width: 543px; height: 542px; border: 2px solid var(--card-edge); }

  .brand-name { position: absolute; color: var(--logo); font-family: "Questrial", sans-serif; line-height: 1; white-space: nowrap; }
  .card--small .brand-name { left: 24px; top: 22px; font-size: 46px; letter-spacing: 3px; }
  .card--square .brand-name { left: 24px; top: 22px; font-size: 100px; letter-spacing: 10px; }

  .name-band { position: absolute; background: var(--band-grey); color: #fff; font-family: "Open Sans", sans-serif; font-weight: 400; white-space: nowrap; }
  .name-band strong { font-weight: 700; }
  .card--small .name-band { left: 260px; top: 24px; right: 0; height: 34px; font-size: 20px; line-height: 34px; padding-left: 6px; letter-spacing: -0.3px; }
  .card--square .name-band { left: 0; right: 0; top: 122px; height: 50px; font-size: 30px; line-height: 50px; text-align: center; letter-spacing: -0.3px; }

  .contact { position: absolute; display: flex; align-items: center; white-space: nowrap; }
  .contact .icon { flex: none; border-radius: 50%; background: var(--band-grey); display: flex; align-items: center; justify-content: center; }
  .contact .icon svg { fill: #fff; }
  .card--small .contact { left: 24px; font-size: 18px; }
  .card--small .contact .icon { width: 38px; height: 38px; margin-right: 9px; }
  .card--small .contact .icon svg { width: 20px; height: 20px; }
  .card--small .contact--phone { top: 114px; }
  .card--small .contact--email { top: 161px; }
  .card--square .contact { left: 24px; font-size: 24px; }
  .card--square .contact .icon { width: 50px; height: 50px; margin-right: 12px; }
  .card--square .contact .icon svg { width: 26px; height: 26px; }
  .card--square .contact--phone { top: 203px; }
  .card--square .contact--email { top: 266px; }

  .address { position: absolute; white-space: nowrap; }
  .card--small .address { right: 24px; top: 100px; font-size: 17px; line-height: 21px; text-align: right; }
  .card--square .address { left: 23px; top: 340px; font-size: 23px; line-height: 27.5px; }

  .tone-strip { position: absolute; left: 0; right: 0; bottom: 0; display: flex; }
  .card--small .tone-strip { height: 25px; }
  .card--square .tone-strip { height: 52px; }
  .tone-strip span { flex: 1; }
  .s1 { background: var(--t1); } .s2 { background: var(--t2); } .s3 { background: var(--t3); }
  .s4 { background: var(--t4); } .s5 { background: var(--t5); } .s6 { background: var(--t6); }
  .s7 { background: var(--t7); } .s8 { background: var(--t8); } .s9 { background: var(--t9); }
  .s10 { background: var(--t10); }
</style>
</head>
<body>

<svg width="0" height="0" style="position:absolute">
  <defs>
    <symbol id="icon-phone" viewBox="0 0 24 24">
      <path d="M8.2 2.5c.6-.3 1.3 0 1.6.6l1.6 3.6c.3.6.1 1.2-.4 1.6l-1.5 1.1c-.3.2-.4.6-.3 1 .6 2.2 1.5 4.4 2.7 6.3.2.3.6.5 1 .4l1.8-.5c.6-.2 1.3.1 1.5.7l1.7 3.5c.3.6.1 1.3-.5 1.6l-1.6.9c-1.2.6-2.7.5-3.7-.4C8.6 19.5 6.3 14.2 6.1 8.9c0-1.3.6-2.5 1.6-3.2z"/>
    </symbol>
    <symbol id="icon-mail" viewBox="0 0 24 24">
      <path d="M2 5h20v14H2zM3.5 6.5v.4L12 13l8.5-6.1v-.4zm0 2.2v8.8h17V8.7L12 14.8z"/>
    </symbol>
  </defs>
</svg>

<section class="card card--small" aria-label="Small card, 70 by 28 mm">
  <div class="brand-name">TULMEX</div>
  <div class="name-band"><strong>NAME</strong>SURNAME</div>
  <div class="contact contact--phone">
    <span class="icon"><svg><use href="#icon-phone"/></svg></span>301 555 2740
  </div>
  <div class="contact contact--email">
    <span class="icon"><svg><use href="#icon-mail"/></svg></span>HI@MARENLOKE.COM
  </div>
  <div class="address">ADDRESS<br>XXXXXXXXXXXXXX<br>XXXXXXXXXXXXXX<br>XXXXXXXXXXXXXX<br>XXXXXXXXXXXXXX</div>
  <div class="tone-strip"><span class="s1"></span><span class="s2"></span><span class="s3"></span><span class="s4"></span><span class="s5"></span><span class="s6"></span><span class="s7"></span><span class="s8"></span><span class="s9"></span><span class="s10"></span></div>
</section>

<section class="card card--square" aria-label="Square card, 65 by 65 mm">
  <div class="brand-name">TULMEX</div>
  <div class="name-band"><strong>NAME</strong>SURNAME</div>
  <div class="contact contact--phone">
    <span class="icon"><svg><use href="#icon-phone"/></svg></span>301 555 2740
  </div>
  <div class="contact contact--email">
    <span class="icon"><svg><use href="#icon-mail"/></svg></span>HI@MARENLOKE.COM
  </div>
  <div class="address">ADDRESS<br>XXXXXXXXXXXXXX<br>XXXXXXXXXXXXXX<br>XXXXXXXXXXXXXX<br>XXXXXXXXXXXXXX</div>
  <div class="tone-strip"><span class="s1"></span><span class="s2"></span><span class="s3"></span><span class="s4"></span><span class="s5"></span><span class="s6"></span><span class="s7"></span><span class="s8"></span><span class="s9"></span><span class="s10"></span></div>
</section>

</body>
</html>
```